Lifestyle brand needs lip balm label design

We need a label design for lip balm tubes. The name of our company is "quorvalent"

Design Description:
Our lip balm tubes will be black. The label itself will be clear/transparent. We would like to create a gradient effect with the color green (same shade as our logo) starting from the bottom and slowly fading out to clear so that the black tube is visible (example of gradient shown in attached image)

We have two lip balm flavors: mint and lemongrass.
We would like the top/clear portion of the label to say "MINT" (all caps) . The second label should say "LEMONGRASS" (all caps) in the same location. Our logo "quorvalent" should be in the bottom/green portion of the label. Below the logo, we would like the words "NATURAL BALM" (all caps) in white text

```html
<!DOCTYPE html>
<html lang="en">
<head>
<meta charset="utf-8">
<title>quorvalent lip balm labels</title>
<link rel="stylesheet" href="https://fonts.googleapis.com/css2?family=Montserrat:wght@400;500&family=Josefin+Sans:wght@300&display=swap">
<style>
  :root {
    --page: #ffffff;
    --tube-black: #000000;
    --deep: #0d0f0a;
    --mid-green: #2a4a18;
    --brand-green: #4a931c;
    --pattern-tint: rgba(74, 147, 28, 0.10);
    --label-white: #ffffff;
    --logo-ink: #262626;
  }
  html, body {
    margin: 0;
    padding: 0;
    width: 1200px;
    height: 531px;
    overflow: hidden;
    background: var(--page);
  }
  .sheet {
    position: relative;
    width: 1200px;
    height: 531px;
  }
  .label {
    position: absolute;
    top: 46px;
    width: 554px;
    height: 442px;
    overflow: hidden;
    background: linear-gradient(to bottom,
      var(--tube-black) 0%,
      var(--deep) 30%,
      var(--mid-green) 62%,
      var(--brand-green) 82%,
      var(--brand-green) 100%);
  }
  .label--lemongrass { left: 46px; }
  .label--mint { left: 607px; width: 555px; height: 440px; }
  .label__pattern {
    position: absolute;
    left: 109px;
    top: 0;
    width: 342px;
    height: 250px;
    background: linear-gradient(to bottom, transparent 0%, var(--pattern-tint) 50%, transparent 100%);
  }
  .label__flavour {
    position: absolute;
    left: 50%;
    transform: translateX(-50%) rotate(180deg);
    writing-mode: vertical-rl;
    margin: 0;
    font-family: "Montserrat", sans-serif;
    font-weight: 400;
    color: var(--label-white);
    line-height: 1;
    white-space: nowrap;
  }
  .label--lemongrass .label__flavour {
    top: 44px;
    font-size: 30px;
    letter-spacing: 0.5px;
  }
  .label--mint .label__flavour {
    top: 45px;
    font-size: 45px;
    font-weight: 500;
    letter-spacing: 2px;
  }
  .label__brand {
    position: absolute;
    left: 0;
    right: 0;
    top: 331px;
    margin: 0;
    text-align: center;
    font-family: "Josefin Sans", sans-serif;
    font-weight: 300;
    font-size: 60px;
    line-height: 1;
    color: var(--logo-ink);
  }
  .label__product {
    position: absolute;
    left: 0;
    right: 0;
    top: 398px;
    margin: 0;
    text-align: center;
    font-family: "Montserrat", sans-serif;
    font-weight: 400;
    font-size: 26px;
    letter-spacing: 0.5px;
    line-height: 1;
    color: var(--label-white);
  }
</style>
</head>
<body>
  <main class="sheet">
    <section class="label label--lemongrass">
      <div class="label__pattern" role="img" aria-label="Area for a radiating green dot burst pattern"></div>
      <h2 class="label__flavour">LEMONGRASS</h2>
      <p class="label__brand">quorvalent</p>
      <p class="label__product">NATURAL BALM</p>
    </section>
    <section class="label label--mint">
      <div class="label__pattern" role="img" aria-label="Area for a radiating green dot burst pattern"></div>
      <h2 class="label__flavour">MINT</h2>
      <p class="label__brand">quorvalent</p>
      <p class="label__product">NATURAL BALM</p>
    </section>
  </main>
</body>
</html>
```